Formlantic Banner Ads

OVERVIEW:

Formlantic is an on-demand, data capture solution that transforms paper, pdf and fax forms into machine readable data with 99% accuracy. Our mission is to unlock the data that drives the world forward. For everyone. We make data capture, easy, affordable and useful for everyone.

These ads should be elegant, professional and convey as sense of how new and different our technology is. We are truly a disruptive solution. Easy to use, fast and highly accurate.

The project is a series of two animated banner ads. These will be displayed on the web as part of our SEM.

Please visit our site (www.formlantic-demo.com) to see our branding, colors and style.

I have attached two versions of our logo.

SPECS:
Each ad should be animated, with two screens and be delivered as a .gif not to exceed 150KB in size for each ad.

Each ad needs to be produced in FOUR sizes. These are:

728x90, 336x280, 120x600 and 300x600

So it is a TOTAL of 8 different ads, each not to exceed 105 KB and each delivered as a .gif.

COPY:

[Ad #1]
Capture data from handwritten forms.

Simple, web-based solution digitizes data, fast. 99% accurate. Free Trial (button)

[Ad #2]

Manage your paper backlog and free your data.

Simple, web-based solution digitizes handwritten forms. Free Trial (button)

Target Market(s)

The target audience is a decision maker in an operations role or a project manager.

Requirements
Must have
• Each ad must not exceed 150 KB in total size.

```html
<!DOCTYPE html>
<html lang="en">
<head>
<meta charset="utf-8">
<title>Formlantic Banner Ads</title>
<link href="https://fonts.googleapis.com/css2?family=Open+Sans:wght@400;600;700;800&family=Roboto+Condensed:wght@300;400;700&family=Nothing+You+Could+Do&display=swap" rel="stylesheet">
<style>
  :root {
    --page-bg: #e8e5e1;
    --blue-light: #3b93e4;
    --blue-mid: #2470cf;
    --blue-deep: #1451ab;
    --accent-blue: #92d0fb;
    --rule-blue: #4aa8f0;
    --white: #ffffff;
    --footer-top: #ffffff;
    --footer-bottom: #eef0f3;
    --logo-ink: #30343b;
    --logo-dot: #1d5fb0;
    --orange-top: #ffbe3a;
    --orange-bottom: #f08600;
    --orange-arrow: #f7941d;
    --frame: #1d1d1d;
    --art-paper: #dfe7f1;
    --art-screen: #c9d4e2;
  }
  * { box-sizing: border-box; margin: 0; padding: 0; }
  html, body { width: 1200px; height: 1037px; overflow: hidden; }
  body { background: var(--page-bg); position: relative; font-family: "Open Sans", sans-serif; color: var(--white); }

  .banner {
    position: absolute;
    border: 1px solid var(--frame);
    background: radial-gradient(ellipse at 50% 45%, var(--blue-light) 0%, var(--blue-mid) 50%, var(--blue-deep) 100%);
    overflow: hidden;
  }
  .banner--half-page { left: 86px; top: 48px; width: 379px; height: 758px; }
  .banner--skyscraper { left: 504px; top: 48px; width: 151px; height: 758px; }
  .banner--rectangle { left: 694px; top: 453px; width: 424px; height: 354px; }
  .banner--leaderboard { left: 86px; top: 846px; width: 920px; height: 114px; }

  .abs { position: absolute; }
  .centered { left: 0; right: 0; text-align: center; }
  .nowrap { white-space: nowrap; }

  .headline { font-weight: 800; line-height: 1; letter-spacing: -0.5px; }
  .headline .accent { color: var(--accent-blue); }
  .script { font-family: "Nothing You Could Do", cursive; font-weight: 400; line-height: 1; }
  .swoosh { display: block; }

  .condensed { font-family: "Roboto Condensed", sans-serif; line-height: 1.05; }
  .condensed .light, .light { font-weight: 300; }
  .condensed .regular, .regular { font-weight: 400; }
  .accent { color: var(--accent-blue); }
  .bold { font-family: "Open Sans", sans-serif; font-weight: 800; }

  .art { border-radius: 4px; }
  .art--forms { background: linear-gradient(160deg, #f4f7fb, var(--art-paper)); box-shadow: 0 0 24px rgba(200,230,255,.55); }
  .art--monitor { background: linear-gradient(180deg, #f5f7fa, var(--art-screen)); box-shadow: 0 0 24px rgba(200,230,255,.55); }

  .footer {
    position: absolute; left: 0; right: 0; bottom: 0;
    background: linear-gradient(180deg, var(--footer-top), var(--footer-bottom));
    border-top: 4px solid var(--rule-blue);
  }
  .brand {
    position: absolute; display: flex; align-items: center; gap: 8px; white-space: nowrap;
    font-family: "Open Sans", sans-serif; font-weight: 400; color: var(--logo-ink);
  }
  .brand__dot { border-radius: 50%; background: var(--logo-dot); flex: none; }

  .cta {
    position: absolute; display: flex; align-items: center; justify-content: center;
    border-radius: 24px; white-space: nowrap;
    background: linear-gradient(180deg, var(--orange-top), var(--orange-bottom));
    box-shadow: 0 2px 3px rgba(0,0,0,.3);
    font-family: "Open Sans", sans-serif; font-weight: 700; color: var(--white);
    text-shadow: 0 1px 1px rgba(150,70,0,.5);
  }
</style>
</head>
<body>

<!-- 300x600 half page -->
<section class="banner banner--half-page">
  <div class="abs centered headline" style="top:34px;font-size:54px;">CAPTURE</div>
  <div class="abs centered headline" style="top:94px;font-size:47px;"><span class="accent">DATA</span> FROM</div>
  <div class="abs centered script" style="top:148px;font-size:40px;">handwritten</div>
  <svg class="abs swoosh" style="left:70px;top:200px" width="240" height="10" viewBox="0 0 240 10"><path d="M2 7 Q120 0 238 6" stroke="#fff" stroke-width="1.5" fill="none"/></svg>
  <div class="abs centered headline" style="top:214px;font-size:46px;">FORMS</div>

  <div class="abs art art--forms" role="img" aria-label="Stack of handwritten paper forms" style="left:22px;top:300px;width:150px;height:148px;"></div>
  <div class="abs art art--monitor" role="img" aria-label="Computer monitor showing digitized data table" style="left:218px;top:300px;width:138px;height:134px;"></div>
  <svg class="abs" style="left:140px;top:330px" width="100" height="90" viewBox="0 0 100 90"><path d="M10 80 Q40 30 78 28" stroke="var(--orange-arrow)" stroke-width="12" fill="none" stroke-linecap="round"/><path d="M70 8 L98 28 L68 48 Z" fill="var(--orange-arrow)"/></svg>

  <div class="abs centered condensed nowrap regular" style="top:512px;font-size:23px;">SIMPLE, WEB-BASED SOLUTION</div>
  <div class="abs centered condensed nowrap light accent" style="top:546px;font-size:37px;">DIGITIZES DATA, FAST.</div>
  <div class="abs centered bold nowrap" style="top:596px;font-size:31px;">99% ACCURATE.</div>

  <div class="footer" style="height:92px;">
    <div class="brand" style="left:18px;top:26px;font-size:27px;"><span class="brand__dot" style="width:30px;height:30px;"></span>Formlantic</div>
    <div class="cta" style="left:214px;top:20px;width:150px;height:46px;font-size:19px;">FREE TRIAL</div>
  </div>
</section>

<!-- 120x600 skyscraper -->
<section class="banner banner--skyscraper">
  <div class="abs centered headline" style="top:16px;font-size:29px;">CAPTURE</div>
  <div class="abs centered headline" style="top:50px;font-size:21px;"><span class="accent">DATA</span> FROM</div>
  <div class="abs centered script" style="top:78px;font-size:21px;">handwritten</div>
  <svg class="abs swoosh" style="left:22px;top:104px" width="108" height="6" viewBox="0 0 108 6"><path d="M2 5 Q54 0 106 4" stroke="#fff" stroke-width="1.2" fill="none"/></svg>
  <div class="abs centered headline" style="top:112px;font-size:25px;">FORMS</div>

  <div class="abs art art--forms" role="img" aria-label="Stack of handwritten paper forms" style="left:24px;top:162px;width:104px;height:110px;"></div>
  <svg class="abs" style="left:56px;top:262px" width="40" height="80" viewBox="0 0 40 80"><path d="M20 4 L20 54" stroke="var(--orange-arrow)" stroke-width="10" stroke-linecap="round"/><path d="M4 50 L36 50 L20 76 Z" fill="var(--orange-arrow)"/></svg>
  <div class="abs art art--monitor" role="img" aria-label="Computer monitor showing digitized data table" style="left:22px;top:334px;width:108px;height:110px;"></div>

  <div class="abs centered condensed nowrap regular" style="top:462px;font-size:16px;">SIMPLE, WEB-BASED</div>
  <div class="abs centered condensed nowrap regular" style="top:481px;font-size:29px;">SOLUTION</div>
  <div class="abs centered condensed nowrap light accent" style="top:514px;font-size:21px;">DIGITIZES DATA,</div>
  <div class="abs centered condensed nowrap light accent" style="top:538px;font-size:38px;">FAST.</div>
  <div class="abs centered bold nowrap" style="top:584px;font-size:14px;">99% ACCURATE.</div>
  <div class="cta" style="left:8px;top:624px;width:135px;height:42px;font-size:16px;">FREE TRIAL</div>

  <div class="footer" style="height:84px;">
    <div class="brand" style="left:10px;top:26px;font-size:19px;gap:5px;"><span class="brand__dot" style="width:20px;height:20px;"></span>Formlantic</div>
  </div>
</section>

<!-- 336x280 rectangle -->
<section class="banner banner--rectangle">
  <div class="abs centered headline nowrap" style="top:20px;font-size:35px;">CAPTURE <span class="accent">DATA</span> FROM</div>
  <div class="abs centered nowrap" style="top:58px;"><span class="script" style="font-size:31px;">handwritten</span> <span class="headline" style="font-size:31px;">FORMS</span></div>
  <svg class="abs swoosh" style="left:72px;top:98px" width="190" height="8" viewBox="0 0 190 8"><path d="M2 6 Q95 0 188 5" stroke="#fff" stroke-width="1.2" fill="none"/></svg>

  <div class="abs art art--forms" role="img" aria-label="Stack of handwritten paper forms" style="left:16px;top:140px;width:108px;height:112px;"></div>
  <div class="abs art art--monitor" role="img" aria-label="Computer monitor showing digitized data table" style="left:150px;top:130px;width:100px;height:104px;"></div>
  <svg class="abs" style="left:94px;top:150px" width="80" height="70" viewBox="0 0 80 70"><path d="M8 62 Q30 26 58 22" stroke="var(--orange-arrow)" stroke-width="10" fill="none" stroke-linecap="round"/><path d="M52 6 L76 22 L50 38 Z" fill="var(--orange-arrow)"/></svg>

  <div class="abs condensed nowrap" style="left:256px;width:156px;top:118px;text-align:center;">
    <div class="regular" style="font-size:16px;">SIMPLE, WEB-BASED</div>
    <div class="regular" style="font-size:29px;">SOLUTION</div>
    <div class="light accent" style="font-size:20px;">DIGITIZES DATA,</div>
    <div class="light accent" style="font-size:38px;">FAST.</div>
    <div class="bold" style="font-size:14px;margin-top:4px;">99% ACCURATE.</div>
  </div>

  <div class="footer" style="height:78px;">
    <div class="brand" style="left:20px;top:20px;font-size:26px;"><span class="brand__dot" style="width:28px;height:28px;"></span>Formlantic</div>
    <div class="cta" style="left:254px;top:14px;width:150px;height:46px;font-size:19px;">FREE TRIAL</div>
  </div>
</section>

<!-- 728x90 leaderboard -->
<section class="banner banner--leaderboard">
  <div class="abs" style="left:0;top:0;width:186px;height:100%;background:linear-gradient(90deg,var(--footer-top),var(--footer-bottom));border-right:4px solid var(--rule-blue);"></div>
  <div class="brand" style="left:14px;top:38px;font-size:22px;gap:7px;"><span class="brand__dot" style="width:24px;height:24px;"></span>Formlantic</div>

  <div class="abs art art--forms" role="img" aria-label="Stack of handwritten paper forms" style="left:198px;top:6px;width:106px;height:100px;"></div>
  <div class="abs art art--monitor" role="img" aria-label="Computer monitor showing digitized data table" style="left:348px;top:6px;width:90px;height:94px;"></div>
  <svg class="abs" style="left:284px;top:30px" width="70" height="56" viewBox="0 0 70 56"><path d="M6 48 Q26 20 50 18" stroke="var(--orange-arrow)" stroke-width="9" fill="none" stroke-linecap="round"/><path d="M44 4 L66 18 L44 32 Z" fill="var(--orange-arrow)"/></svg>

  <div class="abs headline nowrap" style="left:470px;top:14px;font-size:28px;">CAPTURE <span class="accent">DATA</span> FROM</div>
  <div class="abs nowrap" style="left:506px;top:44px;"><span class="script" style="font-size:22px;">handwritten</span> <span class="headline" style="font-size:22px;">FORMS</span></div>
  <div class="abs condensed nowrap" style="left:456px;top:84px;font-size:14px;"><span class="regular">SIMPLE, WEB-BASED SOLUTION</span> <span class="light accent">DIGITIZES DATA,</span> <span class="regular">FAST.</span>&nbsp;&nbsp;<span class="bold" style="font-size:12px;">99% ACCURATE.</span></div>
  <div class="cta" style="left:768px;top:28px;width:138px;height:42px;font-size:18px;">FREE TRIAL</div>
</section>

</body>
</html>
```